Creative cooking instructions label for Lunetta Crepes Batter

Our customers at Lunetta's Crepes have been asking us for 14 years to sell our secret Batter and now we are going to. We have packaged our Regular and Buckwheat Crepe Batter in a small 1quart "mini milk jug" (looks like a regular square milk jug, just 1/4 of the size). We have nutritional info and a small sticker with our name, but need a small 2inch wide, 4 inch long label with short instructions and a small illustrations or something creative as we are a very "hip" and artsy crepe shop. check out our website to get a feel for us. www.lunettascrepes-example.com .

Instructions will be as follows:
1. Shake Batter. Coat the bottom of a 10" pan with BUTTER on medium heat.
2. When Butter bubbles, pour 1/3 regular or 1/4 buckwheat batter in middle of pan.
3. Pick up pan and swirl until batter covers bottom of pan
4. It's ready to flip when the batter is no longer shiny. Use spatula to loosen side, slide spatula under crepe and FLIP!
5. Fill 1/2 of crepe with your FAVORITE fillings!
6. Fold or Roll...and VIOLA!!!
A small sketch is attached but new ideas are welcome!!! A few photos of your shop and food are provided so you can see what we are like.
Label will be printed on silver foiled paper with blue ink.

Target Market(s)

more affluent buyers...price point will be $10 - $12 . People who want to entertain or serve kids family at home. Most of our customers are younger, educated 20-50 year olds.

Industry/Entity Type

Restaurant

Colors
0655a3

Requirements
Must have
• our atmosphere is fun, artistic, creative and personal...we want to make it simple, but creative and fun for the customers
Nice to have
• illistrations would be great, but the space to work with is small..2" wide x 4" long (MAX). Fun words would be good in the instructions
Should not have
• This is a fun, friendly product..not too serious...for example..when cooking, the first crepe may not be good .(may stick to the pan)..opps...but the second will be fantastic!!

```html
<!DOCTYPE html>
<html lang="en">
<head>
<meta charset="utf-8">
<title>Crepe Batter Instructions Label</title>
<link rel="stylesheet" href="https://fonts.googleapis.com/css2?family=Amatic+SC:wght@400;700&family=Kaushan+Script&display=swap">
<style>
  :root {
    --ink: #0655a3;
    --paper: #ffffff;
    --tint: #e7eff8;
    --tint-soft: #f4f8fc;
  }
  * { margin: 0; padding: 0; box-sizing: border-box; }
  html, body { width: 1200px; height: 2400px; overflow: hidden; background: var(--paper); }
  .label {
    position: relative;
    width: 1200px;
    height: 2400px;
    background: var(--paper);
    color: var(--ink);
    font-family: "Amatic SC", "Arial Narrow", sans-serif;
  }
  .label__title {
    position: absolute;
    top: 18px;
    left: 0;
    width: 1200px;
    text-align: center;
    font-family: "Kaushan Script", cursive;
    font-size: 92px;
    line-height: 1.2;
    font-weight: 400;
  }
  .label__rule {
    position: absolute;
    top: 84px;
    width: 300px;
    height: 3px;
    background: var(--ink);
    border-radius: 2px;
  }
  .label__rule--left { left: 64px; }
  .label__rule--right { left: 836px; }

  .step {
    position: absolute;
    left: 56px;
    font-size: 72px;
    line-height: 82px;
    font-weight: 700;
    letter-spacing: 0.5px;
  }
  .step strong {
    font-weight: 700;
    letter-spacing: 2px;
    -webkit-text-stroke: 2.5px var(--ink);
  }
  .step--shake { top: 172px; }
  .step--pour  { top: 572px; }
  .step--swirl { top: 962px; }
  .step--flip  { top: 1272px; }
  .step--fill  { top: 1842px; }
  .step--fold  { top: 2162px; }

  .art {
    position: absolute;
    border-radius: 40px;
    background: radial-gradient(ellipse at center, var(--tint) 0%, var(--tint-soft) 60%, var(--paper) 100%);
  }
  .art--butter-pan { left: 530px; top: 150px; width: 630px; height: 340px; }
  .art--pour       { left: 580px; top: 580px; width: 580px; height: 310px; }
  .art--swirl      { left: 610px; top: 980px; width: 540px; height: 320px; }
  .art--flip       { left: 570px; top: 1310px; width: 590px; height: 410px; }
  .art--fill       { left: 570px; top: 1760px; width: 520px; height: 280px; }
  .art--roll       { left: 520px; top: 2100px; width: 280px; height: 210px; }

  .label__cheer {
    position: absolute;
    left: 780px;
    top: 2150px;
    font-family: "Kaushan Script", cursive;
    font-size: 110px;
    line-height: 1.2;
    transform: rotate(-3deg);
  }
</style>
</head>
<body>
<main class="label">
  <span class="label__rule label__rule--left" aria-hidden="true"></span>
  <h1 class="label__title">Instructions</h1>
  <span class="label__rule label__rule--right" aria-hidden="true"></span>

  <p class="step step--shake">1. Shake Batter.<br>Coat the bottom of<br>a 10" pan with <strong>butter</strong><br>on medium heat.</p>
  <div class="art art--butter-pan" role="img" aria-label="Sketch of a butter dish with a knife above an empty frying pan"></div>

  <p class="step step--pour">2. When Butter bubbles,<br>pour <strong>1/3 regular</strong> or<br><strong>1/4 buckwheat</strong> batter<br>in middle of pan.</p>
  <div class="art art--pour" role="img" aria-label="Sketch of a batter carton pouring drops into a frying pan"></div>

  <p class="step step--swirl">3. Pick up pan and<br><strong>swirl</strong> until batter<br>covers bottom of pan.</p>
  <div class="art art--swirl" role="img" aria-label="Sketch of a hand swirling batter in a frying pan"></div>

  <p class="step step--flip">4. It's ready to flip<br>when the batter is<br>no longer shiny. Use<br>spatula to loosen side,<br>slide spatula under<br>crepe and <strong>flip!</strong></p>
  <div class="art art--flip" role="img" aria-label="Sketch of a crepe flipping in the air above a pan held by a hand, with a spatula"></div>

  <p class="step step--fill">5. Fill 1/2 of crepe<br>with your <strong>favorite</strong><br>fillings!</p>
  <div class="art art--fill" role="img" aria-label="Sketch of a steaming crepe filled with banana slices"></div>

  <p class="step step--fold">6. Fold or Roll...and<br><strong>voila!!!</strong></p>
  <div class="art art--roll" role="img" aria-label="Sketch of a rolled crepe with banana slices showing at the end"></div>

  <p class="label__cheer">Yummy!</p>
</main>
</body>
</html>
```